Waterproofing specialist needs a flyer design

Our company does repair works for any leakage problems, for example, concrete roofs, balcony, toilets & bathroom, etc. We want our flyers to have a certain focus on the home services that we provide, mainly toilets & bathrooms but not leaving out the rest.

For toilet leakages, we use flood infusion method to water proof and repair toilets. Hence, we like to promote there will be No dust, No noise, No smell, No drilling, No hacking and No removal of existing tile finish. The types of chemical used to manage leakage problems are non-toxic and stops re-bar corrosion. Best of all, it only requires only One-day work. We also provide a call for free consultation.

As we do not have a good picture on waterproofing for illustration, you're welcome to come up with your own pictures that deem fit. The design should communicate reliability and safety.
---------------------------------------------------------

Hi, I have uploaded some of our project pictures for your reference. It is to show an example of what we do in waterproofing. We seal up cracked ceilings or walls basically to prevent water leakage. Understood that the pictures came from RUNFrame, as such, I have also done some research. Searching for "Water damage ceiling" is more relevant our profession. However, I did find more pictures from lenvaultery. I have uploaded one example that can be used. Do feedback to me if the uploads helped or more photos are needed to support your design.

Households

Concrete

• Pictures

```html
<!DOCTYPE html>
<html lang="en">
<head>
<meta charset="utf-8">
<title>Tidewell Waterproofing Flyer</title>
<link href="https://fonts.googleapis.com/css2?family=Oswald:wght@300;400&family=Questrial&family=Didact+Gothic&family=Open+Sans:ital,wght@0,400;1,400&family=Roboto+Condensed:ital,wght@1,400&family=PT+Serif:wght@700&display=swap" rel="stylesheet">
<style>
  :root {
    --blue: #1e6fba;
    --blue-mid: #3f8fd3;
    --blue-light: #dbe9f6;
    --blue-pale: #a9d2f2;
    --band: #4a4340;
    --ink: #2b2b2b;
    --grey: #555;
    --shadow: #c8c5dd;
    --white: #fff;
  }
  html, body { margin: 0; padding: 0; overflow: hidden; background: #fff; }
  .flyer { position: relative; width: 846px; height: 1200px; background: var(--white); overflow: hidden; font-family: "Open Sans", sans-serif; }
  .abs { position: absolute; }
  .top-strip { left: 0; top: 0; width: 846px; height: 14px; background: var(--blue); }
  .hero { left: 0; top: 14px; width: 430px; height: 141px; background: linear-gradient(90deg, var(--blue-light) 0%, #8cc0ea 55%, #4f9fdc 100%); }
  .hero-title { right: 16px; top: 24px; margin: 0; font-family: "Oswald", sans-serif; font-weight: 400; font-size: 45px; color: var(--white); letter-spacing: 0.5px; line-height: 1; }
  .hero-sub { right: 18px; top: 86px; margin: 0; font-family: "Roboto Condensed", sans-serif; font-style: italic; font-size: 23px; color: var(--ink); }
  .brand { left: 442px; top: 22px; height: 110px; display: flex; align-items: center; gap: 14px; }
  .brand-mark { width: 54px; height: 54px; border-radius: 50%; background: var(--blue); }
  .brand-name { font-family: "Questrial", sans-serif; font-size: 27px; color: var(--blue); font-weight: 400; line-height: 1.1; }
  .services { left: 0; top: 155px; width: 846px; height: 150px; background: var(--band); text-align: center; }
  .services h1 { margin: 26px 0 0; font-family: "Questrial", sans-serif; font-weight: 400; font-size: 31px; line-height: 39px; letter-spacing: 1.6px; color: var(--blue-pale); -webkit-text-stroke: 0.6px var(--blue-pale); }
  .services p { margin: 4px 0 0; font-style: italic; font-size: 25px; color: var(--white); font-weight: 300; }
  .rule { left: 0; width: 846px; height: 2px; background: var(--band); }
  .photo { box-shadow: 7px 7px 0 var(--shadow); }
  .tab { width: 22px; background: var(--blue); color: var(--white); font-family: "Oswald", sans-serif; font-size: 14px; display: flex; align-items: center; justify-content: center; }
  .tab span { transform: rotate(-90deg); white-space: nowrap; letter-spacing: 0.5px; }
  .tab.after span { transform: rotate(90deg); }
  .caption { left: 0; top: 756px; width: 846px; text-align: center; margin: 0; font-style: italic; font-size: 20px; line-height: 27px; color: var(--blue-mid); }
  .benefits { left: 0; top: 826px; width: 846px; height: 84px; background: var(--band); color: var(--white); text-align: center; font-size: 20.5px; line-height: 30px; text-transform: uppercase; display: flex; align-items: center; justify-content: center; margin: 0; }
  .safety { left: 0; top: 918px; width: 846px; text-align: center; margin: 0; font-family: "Didact Gothic", sans-serif; font-size: 19px; line-height: 24px; color: var(--ink); }
  .divider { left: 55px; top: 973px; width: 737px; height: 1px; background: #999; }
  .oneday { left: 55px; top: 998px; margin: 0; font-family: "PT Serif", serif; font-weight: 700; font-size: 19px; color: var(--blue); }
  .call { left: 53px; top: 1022px; margin: 0; font-family: "Oswald", sans-serif; font-weight: 300; font-size: 29px; color: var(--ink); letter-spacing: 0.8px; }
  .phone { left: 52px; display: flex; align-items: center; gap: 14px; font-family: "Questrial", sans-serif; font-size: 23px; color: var(--blue); letter-spacing: 0.5px; }
  .badge { left: 580px; top: 990px; }
  .footer { left: 0; top: 1152px; width: 846px; height: 48px; background: var(--blue); color: var(--white); font-style: italic; font-size: 19px; }
  .footer .site { position: absolute; left: 60px; top: 11px; }
  .footer .find { position: absolute; left: 318px; top: 11px; }
  .social { position: absolute; top: 14px; width: 21px; height: 21px; border-radius: 50%; background: var(--white); }
</style>
</head>
<body>
<main class="flyer">
  <div class="abs top-strip"></div>

  <header>
    <div class="abs hero">
      <h2 class="abs hero-title">LIVE FREE &amp; CLEAN</h2>
      <p class="abs hero-sub">No more water leakages!</p>
    </div>
    <div class="abs brand">
      <div class="brand-mark"></div>
      <div class="brand-name">Tidewell<br>Waterproofing</div>
    </div>
  </header>

  <section class="abs services">
    <h1>OUR COMPANY DOES REPAIR WORKS<br>FOR ANY LEAKAGE PROBLEMS:</h1>
    <p>concrete roofs, balcony, toilets &amp; bathroom...</p>
  </section>

  <div class="abs rule" style="top:312px"></div>
  <div class="abs rule" style="top:318px;height:1px"></div>

  <div class="abs photo" role="img" aria-label="Concrete roof ledge with weathered grey stains beneath red roof tiles, before repair" style="left:62px;top:347px;width:215px;height:161px;background:linear-gradient(160deg,#8a4a3a 0%,#8a4a3a 22%,#9a9d98 30%,#b9bab4 65%,#c98a55 80%,#b67744 100%)"></div>
  <div class="abs photo" role="img" aria-label="Bathroom ceiling corner with yellow water-damaged walls and a small window" style="left:289px;top:347px;width:268px;height:161px;background:linear-gradient(180deg,#ececea 0%,#e2e1dc 45%,#e6d66f 70%,#d8c35a 100%)"></div>
  <div class="abs photo" role="img" aria-label="Repaired roof ledge with a clean white waterproof coating under red roof tiles" style="left:571px;top:347px;width:215px;height:161px;background:linear-gradient(160deg,#8a4a3a 0%,#8a4a3a 22%,#f0f0ef 32%,#e8e8e6 62%,#d9955d 78%,#c47d45 100%)"></div>
  <div class="abs photo" role="img" aria-label="Toilet and wash basin with beige floor tiles, before waterproofing" style="left:62px;top:538px;width:358px;height:201px;background:linear-gradient(180deg,#d9d9d7 0%,#ececea 45%,#d8c8ae 70%,#c9b596 100%)"></div>
  <div class="abs photo" role="img" aria-label="Toilet floor covered with white waterproof coating and an orange chemical container" style="left:431px;top:538px;width:357px;height:201px;background:linear-gradient(180deg,#dcdcda 0%,#f0f0ee 45%,#f6f6f4 75%,#e9e9e7 100%)"></div>

  <div class="abs tab before" style="left:30px;top:483px;height:79px"><span>BEFORE</span></div>
  <div class="abs tab after" style="left:799px;top:485px;height:82px"><span>AFTER</span></div>

  <p class="abs caption">For toilet leakages, we use flood infusion method<br>to water proof and repair toilets.</p>

  <p class="abs benefits">Hence, there will be no dust, no noise, no smell, no drilling,<br>no hacking and no removal of existing tile finish.</p>

  <p class="abs safety">The types of chemical used to manage leakage problems<br>are non-toxic and stops re-bar corrosion.</p>
  <div class="abs divider"></div>

  <p class="abs oneday">Yes! it requires only One-day work.</p>
  <p class="abs call">CALL FOR FREE CONSULTATION</p>

  <div class="abs phone" style="top:1068px">
    <svg width="24" height="30" viewBox="0 0 24 30" fill="none" stroke="#1e6fba" stroke-width="1.6"><rect x="6" y="8" width="11" height="20" rx="2" transform="rotate(-12 11 18)"/><path d="M4 6a7 7 0 0 1 8-4M6 8a4 4 0 0 1 5-3"/></svg>
    <span>+91-9000012345</span>
  </div>
  <div class="abs phone" style="top:1101px">
    <svg width="26" height="26" viewBox="0 0 26 26" fill="none" stroke="#1e6fba" stroke-width="1.6"><circle cx="13" cy="13" r="11.5"/><path d="M9 7c-1 1-2 2-1 4 1 3 4 6 7 7 2 1 3 0 4-1l-2-2-2 1c-2-1-3-2-4-4l1-2z" fill="#1e6fba" stroke="none"/></svg>
    <span>+011-4000-1234</span>
  </div>

  <svg class="abs badge" width="215" height="140" viewBox="0 0 215 140" aria-label="Quality works guaranteed">
    <polygon fill="#1e6fba" points="107,0 117,12 132,6 137,21 153,20 152,36 167,42 160,56 171,68 158,77 162,93 146,96 141,111 126,107 117,120 107,110 97,120 88,107 73,111 68,96 52,93 56,77 43,68 54,56 47,42 62,36 61,20 77,21 82,6 97,12"/>
    <circle cx="107" cy="60" r="47" fill="none" stroke="#fff" stroke-width="1.5"/>
    <polygon fill="#1a5fa0" points="10,72 44,70 44,102 10,104 22,88"/>
    <polygon fill="#1a5fa0" points="205,72 171,70 171,102 205,104 193,88"/>
    <path d="M35 72 Q107 60 180 72 L180 100 Q107 88 35 100 Z" fill="#3a8ad0" stroke="#fff" stroke-width="1.2"/>
    <text x="107" y="44" text-anchor="middle" font-family="Oswald, sans-serif" font-size="12" fill="#fff">QUALITY</text>
    <text x="107" y="60" text-anchor="middle" font-family="Oswald, sans-serif" font-size="12" fill="#fff">WORKS</text>
    <text x="107" y="93" text-anchor="middle" font-family="Oswald, sans-serif" font-size="19" fill="#fff" letter-spacing="1">GUARANTEED</text>
  </svg>

  <footer class="abs footer">
    <span class="site">www.dryhomefix.com</span>
    <span class="find">also find us at:</span>
    <span class="social" style="left:680px"></span>
    <span class="social" style="left:709px"></span>
    <span class="social" style="left:738px"></span>
    <span class="social" style="left:767px"></span>
  </footer>
</main>
</body>
</html>
```